Startup online payment business - Sporting / Golf, Swift Tee payment

Background:
Our business name is "Swift Tee" we provide online payments for golfing services via our website. We currently have a logo used on our website. No other design style has been developed. Our aim is to remove cash payments for service at golf clubs.

Our Key Values:
Quick and easy
Formal and polite
Fun with professional boundary
Mate-ship relationships
100% online digital

What we want from you:
Marketing design to be used on posters and stickers in a retail setting to direct customers to our online payment Chanel.
Design must incorporate attached logo, URL swifttee.com.au and our key values can act as a guide the type of design. We have used color Hex#007672 for logo background. We are open to use other colors.

Target Market(s)

Golf clubs and golf players

Industry/Entity Type

Golf Course

Font styles to use
Sans Serif

Requirements
Must have
• Directions to online payment via URL: swifttee.com.au
Nice to have
• We like the idea of the slogan: No Cash - No worries. Have attached home screen that will be available from URL link. Consideration if using mobile phone in image. Push the online payment and steps 1. Visit swifttee.com 2. Select club 3. Confirm payment
Should not have
• Cartoons

```html
<!DOCTYPE html>
<html lang="en">
<head>
<meta charset="utf-8">
<title>Swift Tee – No Cash, No worries poster</title>
<link rel="stylesheet" href="https://fonts.googleapis.com/css2?family=Rubik:ital,wght@0,300;0,400;0,500;0,700;0,800;0,900;1,700;1,800&family=Lato:wght@400;700&display=swap">
<style>
  :root {
    --teal: #007672;
    --white: #ffffff;
    --ink: #111414;
    --sky-top: #3f8fd8;
    --sky-low: #8cc3ec;
    --tree: #4f8a2e;
    --grass: #a9c95a;
    --grass-light: #c4da78;
    --stage: #e8ebe6;
    --phone-body: #f2f3f5;
    --field: #e6e8ee;
  }
  * { margin: 0; padding: 0; box-sizing: border-box; }
  html, body { width: 1067px; height: 1200px; overflow: hidden; }
  body { background: var(--stage); font-family: "Rubik", sans-serif; position: relative; }

  .poster {
    position: absolute; left: 124px; top: 20px;
    width: 818px; height: 1160px; overflow: hidden;
    background: var(--sky-top);
  }
  .course-photo {
    position: absolute; inset: 0;
    background: linear-gradient(180deg, var(--sky-top) 0%, var(--sky-low) 46%, var(--tree) 52%, #3f7426 62%, var(--grass) 68%, var(--grass-light) 86%);
  }

  .headline {
    position: absolute; left: 150px; top: 30px;
    color: var(--white); font-weight: 900; font-size: 100px;
    line-height: 1; letter-spacing: -1px;
  }
  .headline-rule {
    position: absolute; left: 232px; top: 252px; width: 392px;
    height: 2px; background: var(--white);
  }
  .lead {
    position: absolute; left: 228px; top: 266px;
    color: var(--ink); font-weight: 700; font-style: italic; font-size: 30px;
  }
  .url {
    position: absolute; left: 222px; top: 300px;
    color: var(--teal); font-weight: 800; font-size: 66px; letter-spacing: -1px;
  }

  .steps-tab {
    position: absolute; left: 110px; top: 705px; width: 460px; height: 60px;
    background: var(--teal); border-radius: 18px 0 0 18px;
    color: var(--white); font-weight: 800; font-size: 40px;
    padding: 4px 0 0 22px;
  }
  .steps { position: absolute; left: 122px; top: 782px; list-style: none; }
  .steps li {
    display: flex; align-items: center; gap: 18px; height: 46px; margin-bottom: 2px;
    color: var(--ink); font-weight: 500; font-size: 33px;
  }
  .step-num {
    flex: none; width: 40px; height: 40px; border-radius: 50%; background: var(--teal);
    color: var(--white); font-size: 22px; font-weight: 500;
    display: flex; align-items: center; justify-content: center;
  }
  .steps em { font-weight: 800; }

  .values-band { position: absolute; left: 0; top: 935px; width: 818px; height: 225px; }
  .values {
    position: absolute; left: 50px; top: 978px; list-style: none;
    color: var(--white); font-weight: 400; font-size: 25px; line-height: 32px;
  }
  .values li::before { content: "•"; margin-right: 16px; }

  .phone {
    position: absolute; left: 518px; top: 690px; width: 290px; height: 520px;
    background: var(--phone-body); border-radius: 40px;
    box-shadow: inset 0 0 0 2px #d6d8dc;
  }
  .phone-camera { position: absolute; left: 84px; top: 38px; width: 9px; height: 9px; border-radius: 50%; background: #2b2f38; }
  .phone-speaker { position: absolute; left: 116px; top: 41px; width: 60px; height: 5px; border-radius: 3px; background: #2b2f38; }
  .screen {
    position: absolute; left: 16px; top: 78px; width: 258px; height: 440px;
    background: var(--teal); color: var(--white);
    font-family: "Lato", sans-serif; padding: 12px 14px;
  }
  .screen-top { display: flex; justify-content: space-between; align-items: flex-start; }
  .login-btn { border: 1px solid var(--white); border-radius: 6px; font-size: 10px; padding: 3px 7px; }
  .menu-btn { margin-top: 26px; border: 1px solid var(--white); border-radius: 4px; width: 26px; height: 24px; display: flex; align-items: center; justify-content: center; font-size: 14px; }
  .brand-name {
    position: absolute; left: 0; right: 0; top: 44px; text-align: center;
    font-family: "Rubik", sans-serif; font-weight: 700; font-size: 26px;
  }
  .welcome { margin-top: 52px; font-size: 15px; text-decoration: underline; text-underline-offset: 4px; }
  .intro { margin-top: 8px; font-size: 9.5px; line-height: 1.4; }
  .label { margin-top: 12px; font-size: 13px; }
  .search {
    margin-top: 8px; height: 26px; background: var(--field); color: #777c86;
    font-size: 10px; display: flex; align-items: center; gap: 8px; padding-left: 26px;
  }
  .counter-row { margin-top: 10px; display: flex; align-items: center; gap: 8px; }
  .stepper { display: flex; border: 2px solid var(--white); border-radius: 3px; }
  .stepper span { width: 26px; height: 22px; display: flex; align-items: center; justify-content: center; font-size: 16px; }
  .stepper span + span { border-left: 2px solid var(--white); }
  .count { width: 42px; height: 24px; background: var(--white); color: var(--ink); font-size: 10px; display: flex; align-items: center; justify-content: center; }
  .holes { margin-left: auto; display: flex; align-items: center; gap: 5px; font-size: 8px; }
  .toggle { width: 34px; height: 18px; border-radius: 9px; background: var(--white); }
  .total { margin-top: 12px; font-size: 13px; }
  .submit { margin-top: 12px; height: 30px; background: #4a4f5c; text-align: center; font-size: 12px; line-height: 30px; }
</style>
</head>
<body>
  <main class="poster">
    <div class="course-photo" role="img" aria-label="Sunny golf course photo: a golfer leaping in celebration with a putter raised, a flag pin on the green, a golf cart and trees under a blue sky"></div>

    <h1 class="headline">No Cash...<br>No worries!</h1>
    <div class="headline-rule"></div>
    <p class="lead">Pay all your golfing fees through</p>
    <p class="url">swifttee.com.au</p>

    <div class="steps-tab">3 easy steps</div>
    <ol class="steps">
      <li><span class="step-num">1</span><span>Visit <em>swifttee.com</em></span></li>
      <li><span class="step-num">2</span><span>Select club</span></li>
      <li><span class="step-num">3</span><span>Confirm payment</span></li>
    </ol>

    <svg class="values-band" viewBox="0 0 818 225" preserveAspectRatio="none" aria-hidden="true">
      <path d="M0 26 Q120 4 300 10 T818 40 V225 H0 Z" fill="#ffffff"/>
      <path d="M0 34 Q120 12 300 18 T818 48 V225 H0 Z" fill="#007672"/>
    </svg>
    <ul class="values">
      <li>Quick and easy</li>
      <li>Formal and polite</li>
      <li>Fun with professional boundary</li>
      <li>Mate-ship relationships</li>
      <li>100% online digital</li>
    </ul>

    <div class="phone">
      <span class="phone-camera"></span>
      <span class="phone-speaker"></span>
      <div class="screen">
        <div class="screen-top">
          <span class="login-btn">Login</span>
          <span class="menu-btn">&#8801;</span>
        </div>
        <div class="brand-name">Swift Tee</div>
        <p class="welcome">Welcome to Swift Tee.</p>
        <p class="intro">You can pay your Swift Tee fees for participating clubs here.</p>
        <p class="label">Choose your Club</p>
        <div class="search">
          <svg width="11" height="11" viewBox="0 0 12 12" aria-hidden="true"><circle cx="5" cy="5" r="3.8" fill="none" stroke="#777c86" stroke-width="1.3"/><path d="M8 8 L11 11" stroke="#777c86" stroke-width="1.3"/></svg>
          Type the Name of your Club
        </div>
        <p class="label">How many Players and Holes</p>
        <div class="counter-row">
          <div class="stepper"><span>&minus;</span><span>+</span></div>
          <div class="count">4</div>
          <div class="holes">9 <span class="toggle"></span> 18</div>
        </div>
        <p class="total">Greens Total: $15.00</p>
        <div class="submit">Submit</div>
      </div>
    </div>
  </main>
</body>
</html>
```